Quiet Verses Across Winter Evenings

Need a BOOK COVER, SPINE, and BACK for above named book. This is the story of my late wife (a university professor) told through her own songs and poems. It is about the people she loved, especially her grand children, her extensive professional and life interests, her family, friends, and festivities, her illness, etc.
Updates

Need extra days to review

Target Market(s)

Family and friends

Font styles to use
Other font styles liked:
• Times New Roman

Requirements
Must have
• Regret I haven't given much thought to it...
Nice to have
• Regret I haven't given much thought to it..
Should not have

```html
<!DOCTYPE html>
<html lang="en">
<head>
<meta charset="utf-8">
<title>Quiet Verses Across Winter Evenings — Cover Wrap</title>
<link rel="stylesheet" href="https://fonts.googleapis.com/css2?family=Libre+Baskerville:wght@400;700&family=Roboto+Slab:wght@700;800&display=swap">
<style>
  :root {
    --stage: #4a4a4a;
    --teal-light: #dff5f0;
    --teal: #8fd6c9;
    --teal-deep: #5cb8ab;
    --gold: #d9a654;
    --gold-deep: #b8822e;
    --cream: #f6eedc;
    --title-red: #c0392b;
    --title-red-dark: #9e2a1f;
    --ink: #111111;
    --white: #ffffff;
    --tree-leaf: #b5642c;
  }
  * { box-sizing: border-box; margin: 0; padding: 0; }
  html, body { width: 1200px; height: 675px; overflow: hidden; background: var(--stage); }
  .wrap {
    position: absolute; left: 132px; top: 8px;
    width: 935px; height: 660px; overflow: hidden;
    font-family: "Libre Baskerville", "Times New Roman", serif;
  }
  .panel { position: absolute; top: 0; height: 100%; overflow: hidden; }
  .back { left: 0; width: 437px;
    background: linear-gradient(170deg, var(--teal-deep) 0%, var(--teal) 35%, var(--teal-light) 75%, #eef6ef 100%); }
  .spine { left: 437px; width: 61px;
    background: linear-gradient(180deg, var(--teal) 0%, var(--teal-light) 45%, #f3efe2 80%, #e9dcc0 100%); }
  .front { left: 498px; width: 437px;
    background: linear-gradient(120deg, var(--teal) 0%, var(--teal-light) 32%, var(--cream) 52%, var(--gold) 80%, var(--gold-deep) 100%); }
  .tree {
    position: absolute; left: 35px; top: 344px; width: 368px; height: 265px;
    border-radius: 50% 50% 8% 8% / 60% 60% 10% 10%;
    background: radial-gradient(ellipse at 50% 40%, var(--tree-leaf) 0%, rgba(181,100,44,.55) 45%, rgba(58,42,32,.35) 75%, transparent 100%);
  }
  .ground {
    position: absolute; left: 0; bottom: 0; width: 100%; height: 110px;
    background: linear-gradient(180deg, rgba(0,0,0,0) 0%, rgba(0,0,0,.85) 45%, var(--ink) 70%);
  }
  .author {
    position: absolute; left: 0; bottom: 22px; width: 100%; text-align: center;
    font-family: "Roboto Slab", Georgia, serif; font-weight: 800;
    font-size: 23px; color: var(--white); letter-spacing: .5px;
  }
  .quote-card {
    position: absolute; left: 43px; top: 158px; width: 352px; height: 116px;
    background: rgba(224, 247, 241, .9); border-radius: 16px;
    box-shadow: 0 3px 8px rgba(0,0,0,.25);
    padding: 46px 26px 0 28px; text-align: center;
  }
  .quote-card p { font-size: 10px; line-height: 1.15; color: var(--title-red); letter-spacing: .3px; }
  .quote-mark { position: absolute; font-size: 22px; font-weight: 700; color: var(--ink); }
  .quote-mark.open { left: 9px; top: 36px; }
  .quote-mark.close { right: 10px; top: 86px; }
  .quote-credit { position: absolute; right: 30px; bottom: 7px; font-size: 7.5px; font-weight: 700; color: var(--ink); }
  .portrait {
    position: absolute; left: 182px; top: 119px; width: 75px; height: 75px;
    border-radius: 50%; background: radial-gradient(circle, var(--white) 55%, #d9d9d9 100%);
    box-shadow: 0 2px 5px rgba(0,0,0,.3);
  }
  .spine-text {
    position: absolute; left: 50%; transform: translateX(-50%);
    writing-mode: vertical-rl; white-space: nowrap;
    font-weight: 700; color: var(--ink);
  }
  .spine-title { top: 120px; font-size: 13px; line-height: 1.2; text-align: center; }
  .spine-author { top: 392px; font-family: "Roboto Slab", Georgia, serif; font-size: 14px; }
  .title {
    position: absolute; left: 0; width: 100%; text-align: center;
    font-weight: 700; color: var(--title-red);
    text-shadow: 1px 2px 2px rgba(90,20,10,.45);
  }
  .title-top { top: 122px; font-size: 34px; }
  .title-link {
    position: absolute; left: 189px; top: 170px; width: 58px; height: 58px; border-radius: 50%;
    background: radial-gradient(circle at 40% 35%, var(--title-red), var(--title-red-dark));
    color: var(--cream); font-size: 12px; line-height: 58px; text-align: center;
  }
  .title-bottom { top: 232px; font-size: 36px; }
</style>
</head>
<body>
  <div class="wrap">
    <section class="panel back">
      <div class="quote-card">
        <span class="quote-mark open">&ldquo;</span>
        <p>Lorem ipsum dolor sit amet, consectetur adipiscing elit, sed do eiusmod tempor incididunt ut labore et dolore magna aliqua. Ut enim ad minim veniam, quis nostrud exercitation ullamco laboris nisi ut aliquip ex ea</p>
        <span class="quote-mark close">&rdquo;</span>
        <span class="quote-credit">Meera Kulkarni Rao</span>
      </div>
      <div class="portrait" role="img" aria-label="Silhouette of a couple holding hands"></div>
      <div class="tree" role="img" aria-label="Illustrated tree with autumn leaves"></div>
      <div class="ground"></div>
      <div class="author">Meera Kulkarni Rao</div>
    </section>

    <section class="panel spine">
      <div class="spine-text spine-title">Quiet Verses Across<br>Winter Evenings</div>
      <div class="spine-text spine-author">Meera Kulkarni Rao</div>
    </section>

    <section class="panel front">
      <h1 class="title title-top">Quiet Verses</h1>
      <div class="title-link">Across</div>
      <h1 class="title title-bottom">Winter Evenings</h1>
      <div class="tree" role="img" aria-label="Illustrated tree with autumn leaves"></div>
      <div class="ground"></div>
      <div class="author">Meera Kulkarni Rao</div>
    </section>
  </div>
</body>
</html>
```